Branding Package for an environmental water treatment operations company
Use the provided Logo. The name of the company is Coordinated Ecological Solutions or CES
Branding Package for an environmental water treatment operations company - Environment
Creative Brief
Professional
Mark Delane
President
217 Thornbury Ave Canonsburg, PA. 15317
tkvallen@mailbrook.net
U have freedom to experiment with any fonts to find the best match.
I will add to this later as I see what's being submitted.

```html
<!DOCTYPE html>
<html lang="en">
<head>
<meta charset="UTF-8">
<title>Coordinated Ecological Solutions Business Card</title>
<link href="https://fonts.googleapis.com/css2?family=Raleway:wght@300;400&display=swap" rel="stylesheet">
<style>
  :root {
    --page-bg: #e9e6e1;
    --card-bg: #ffffff;
    --card-edge: #5b6a8f;
    --text-main: #5f6870;
    --text-soft: #8a939b;
    --rule: #c9ced3;
  }
  * { box-sizing: border-box; margin: 0; padding: 0; }
  html, body {
    width: 1200px; height: 1023px; overflow: hidden;
    background: var(--page-bg);
    font-family: "Raleway", sans-serif;
  }
  .sheet {
    width: 1200px; height: 1023px;
    display: flex; flex-direction: column;
    align-items: center; justify-content: center;
    gap: 40px;
  }
  .card {
    width: 800px; height: 457px;
    background: var(--card-bg);
    box-shadow: 0 2px 10px rgba(0,0,0,0.12);
    position: relative;
  }
  .card--front { border-left: 10px solid var(--card-edge); display: flex; align-items: center; }
  .company {
    width: 330px; padding-left: 56px; padding-right: 30px;
    font-size: 24px; font-weight: 400; line-height: 1.3;
    color: var(--text-main); letter-spacing: 0.5px;
  }
  .divider { width: 1px; height: 300px; background: var(--rule); flex: none; }
  .contact { padding-left: 48px; color: var(--text-main); }
  .contact__name { font-size: 26px; font-weight: 400; letter-spacing: 1px; text-transform: uppercase; }
  .contact__title { font-size: 14px; font-weight: 300; letter-spacing: 2px; text-transform: uppercase; color: var(--text-soft); margin-top: 4px; }
  .contact__rule { width: 240px; height: 1px; background: var(--rule); margin: 26px 0; }
  .contact__line { font-size: 15px; font-weight: 400; line-height: 1.7; text-transform: uppercase; letter-spacing: 0.5px; display: flex; align-items: center; gap: 10px; }
  .contact__line--email { text-transform: none; }
  .contact__gap { height: 14px; }
  .icon { width: 14px; height: 14px; flex: none; }
  .card--back { display: flex; align-items: center; justify-content: center; }
  .card--back .company { width: auto; padding: 0; text-align: center; font-size: 22px; }
</style>
</head>
<body>
<main class="sheet">
  <section class="card card--front">
    <p class="company">Coordinated Ecological Solutions</p>
    <div class="divider"></div>
    <div class="contact">
      <p class="contact__name">Mark Delane</p>
      <p class="contact__title">President</p>
      <div class="contact__rule"></div>
      <p class="contact__line">217 Thornbury Ave</p>
      <p class="contact__line">Canonsburg, PA. 15317</p>
      <div class="contact__gap"></div>
      <p class="contact__line">
        <svg class="icon" viewBox="0 0 16 16"><path d="M4 1l3 3-2 2c1 2 3 4 5 5l2-2 3 3-2 3C7 15 1 9 1 3z" fill="#8a939b"/></svg>
        (412) 555-0148
      </p>
      <p class="contact__line">
        <svg class="icon" viewBox="0 0 16 16"><rect x="2" y="5" width="12" height="8" fill="none" stroke="#8a939b" stroke-width="1.5"/><rect x="4" y="2" width="8" height="4" fill="#8a939b"/></svg>
        (724) 555-0192
      </p>
      <p class="contact__line contact__line--email">
        <svg class="icon" viewBox="0 0 16 16"><rect x="1" y="3" width="14" height="10" fill="none" stroke="#8a939b" stroke-width="1.5"/><path d="M1 3l7 6 7-6" fill="none" stroke="#8a939b" stroke-width="1.5"/></svg>
        tkvallen@mailbrook.net
      </p>
    </div>
  </section>
  <section class="card card--back">
    <p class="company">Coordinated Ecological Solutions</p>
  </section>
</main>
</body>
</html>
```